BFCM Creatives Theme

We are looking for an initial design for our BFCM campaign this year to set the theme for all other creatives for BFCM. We are an ecommerce brand selling Merino wool baby clothing. Our flagship product is the Cozy Nestling Drift Cocoon (see images).

We are starting with the request for an instagram post, announcing the sale (details below). This post should be 1080x1350 but also look appealing in the square grid. I've attached a basic brand card showing color palette, fonts, and logos. I will also attach some image options. We are looking for your creativity to shine while aligning with our branding and connecting with the customer. If you have a specific idea and are looking for a specific image please contact us.

Sale Details:
- 20% Off Sitewide
- 11.28.24 - 12.02.24
- Excluding giftcards and imperfects. No rainchecks.

```html
<!DOCTYPE html>
<html lang="en">
<head>
<meta charset="utf-8">
<title>Lanella BFCM Sale Post</title>
<link rel="stylesheet" href="https://fonts.googleapis.com/css2?family=Poppins:wght@600;700;800&family=Caveat:wght@500&display=swap">
<style>
  :root {
    --stone: #a9a699;
    --charcoal: #343538;
    --linen: #f0efed;
    --white: #ffffff;
    --photo-light: #e4e5df;
    --photo-mid: #c9d0bd;
    --photo-deep: #adbd98;
    --backdrop: #e6e5e2;
  }
  * { margin: 0; padding: 0; box-sizing: border-box; }
  html, body {
    width: 1200px; height: 1197px; overflow: hidden;
    background: var(--backdrop);
  }
  .post-frame {
    position: absolute; left: 121px; top: 0;
    width: 1080px; height: 1350px;
    transform: scale(0.8867); transform-origin: top left;
    background: var(--stone);
    overflow: hidden;
    font-family: "Poppins", sans-serif;
  }
  .hero-photo {
    position: absolute; left: 0; top: 0; width: 636px; height: 1350px;
    background: linear-gradient(160deg, var(--photo-light) 0%, var(--photo-mid) 45%, var(--photo-deep) 100%);
  }
  .block { position: absolute; }
  .top-bar { left: 0; top: 0; width: 340px; height: 32px; background: var(--charcoal); }
  .corner-square { left: 33px; top: 54px; width: 86px; height: 86px; background: var(--charcoal); }
  .stripe { background: var(--linen); }
  .stripe-top-1 { left: 926px; top: 23px; width: 154px; height: 24px; }
  .stripe-top-2 { left: 926px; top: 75px; width: 154px; height: 24px; }
  .stripe-left-1 { left: 0; top: 1010px; width: 153px; height: 24px; background: var(--white); }
  .stripe-left-2 { left: 0; top: 1062px; width: 153px; height: 24px; background: var(--white); }
  .bottom-box { left: 531px; top: 1255px; width: 549px; height: 95px; background: var(--charcoal); }

  .headline {
    position: absolute; left: 672px; top: 163px;
    color: var(--white); font-weight: 800; font-size: 186px;
    line-height: 172px; letter-spacing: -2px;
  }
  .sitewide-band {
    position: absolute; left: 636px; top: 504px; width: 444px; height: 111px;
    background: var(--linen);
    display: flex; align-items: center; padding-left: 38px;
  }
  .sitewide-band span { color: var(--charcoal); font-weight: 700; font-size: 86px; line-height: 1; }
  .calendar-icon { position: absolute; left: 816px; top: 654px; width: 72px; height: 76px; }
  .sale-dates {
    position: absolute; left: 636px; width: 444px; top: 734px; text-align: center;
    color: var(--white); font-weight: 700; font-size: 47px; letter-spacing: -0.5px; line-height: 1.2;
  }
  .terms {
    position: absolute; left: 686px; top: 820px; width: 390px;
    list-style: none; color: var(--white);
    font-family: "Caveat", cursive; font-size: 49px; line-height: 54px;
  }
  .terms li { position: relative; padding-left: 37px; margin-bottom: 20px; }
  .terms li::before {
    content: ""; position: absolute; left: 0; top: 24px;
    width: 13px; height: 13px; border-radius: 50%; background: var(--white);
  }
  .brand-band {
    position: absolute; left: 368px; top: 1048px; width: 712px; height: 90px;
    background: var(--linen);
    display: flex; align-items: center; padding-left: 130px; gap: 18px;
  }
  .brand-dot { width: 56px; height: 56px; border-radius: 50%; border: 4px solid var(--charcoal); }
  .brand-name { color: var(--charcoal); font-weight: 600; font-size: 62px; line-height: 1; }
</style>
</head>
<body>
  <main class="post-frame">
    <div class="hero-photo" role="img" aria-label="Photo of a baby wearing a sage green leaf-print merino sleep sack in a white crib"></div>

    <div class="block top-bar"></div>
    <div class="block corner-square"></div>
    <div class="block stripe stripe-top-1"></div>
    <div class="block stripe stripe-top-2"></div>
    <div class="block stripe-left-1"></div>
    <div class="block stripe-left-2"></div>

    <h1 class="headline">20%<br>OFF</h1>

    <div class="sitewide-band"><span>Sitewide</span></div>

    <svg class="calendar-icon" viewBox="0 0 72 76" aria-hidden="true">
      <rect x="3" y="10" width="66" height="62" rx="9" fill="none" stroke="#fff" stroke-width="5"/>
      <rect x="3" y="10" width="66" height="14" rx="6" fill="#fff"/>
      <rect x="16" y="2" width="7" height="16" rx="3" fill="#fff"/>
      <rect x="49" y="2" width="7" height="16" rx="3" fill="#fff"/>
      <g fill="#fff">
        <rect x="12" y="32" width="9" height="8"/><rect x="25" y="32" width="9" height="8"/><rect x="38" y="32" width="9" height="8"/><rect x="51" y="32" width="9" height="8"/>
        <rect x="12" y="44" width="9" height="8"/><rect x="25" y="44" width="9" height="8"/><rect x="38" y="44" width="9" height="8"/><rect x="51" y="44" width="9" height="8"/>
        <rect x="12" y="56" width="9" height="8"/><rect x="25" y="56" width="9" height="8"/><rect x="38" y="56" width="9" height="8"/>
      </g>
    </svg>

    <p class="sale-dates">11.28.24 - 12.02.24</p>

    <ul class="terms">
      <li>Excluding giftcards and imperfects</li>
      <li>No rainchecks</li>
    </ul>

    <div class="brand-band">
      <span class="brand-dot"></span>
      <span class="brand-name">Lanella</span>
    </div>

    <div class="block bottom-box"></div>
  </main>
</body>
</html>
```